Natural Frond product needs a new Label design

We supply premium quality 'Amber Frond' from the pristine waters of South Eastern Australia, for human consumption.  The company has been operating since 1965.
Frond (seaweed) is a type of superfood and is used as a health supplement  - high in vitamins, minerals, fibre and iodine.
Many people benefit from kelp - however the target market is health food stores and their customers. The look should be organic/natural/simple clean and fresh. I have also thought about a retro 60's look as that was when the product was first established. There are currently two products - granules and powder and 2 sizes.
I have uploaded the current label, which was produced more than 10 years ago and needs updating.
The label will either be reproduced as stickers or printed directly onto the new packaging which will be food grade cardboard tubes such as those used for packaging tea. (see Markotra for samples)
The word Frond should be highlighted and perhaps larger than “Amber”.
The company is called Tidewell Goods and I have uploaded a logo as well as the ‘embossed’ look and feel I like.

Target Market(s)
Health food stores, wellness industry, organic buyers
Industry/Entity Type
Health And Wellness
Requirements
Must have
- Tidewell Good Logo, natural look and feel

Nice to have
- Embossed look, sand/sandpaper type background

```html
<!DOCTYPE html>
<html lang="en">
<head>
<meta charset="utf-8">
<title>Amber Frond Meal – Label</title>
<link rel="stylesheet" href="https://fonts.googleapis.com/css2?family=Playfair+Display:wght@400;500&family=Dancing+Script:wght@500;700&display=swap">
<style>
  :root {
    --kraft: #c9a67e;
    --kraft-dark: #b8936a;
    --label: #ffffff;
    --olive: #8c9c3a;
    --olive-light: #9fb04a;
    --leaf: #6f9a3c;
    --leaf-light: #a9c77a;
    --ink: #3b2a22;
  }
  html, body {
    margin: 0;
    padding: 0;
    width: 1085px;
    height: 1200px;
    overflow: hidden;
    background: var(--kraft);
  }
  .canvas {
    position: relative;
    width: 1085px;
    height: 1200px;
    background: radial-gradient(circle at 50% 50%, var(--kraft) 0%, var(--kraft-dark) 100%);
  }
  .label-art { position: absolute; inset: 0; }
  .title {
    font-family: "Playfair Display", serif;
    fill: var(--olive);
    text-anchor: middle;
  }
  .brand-name {
    font-family: "Playfair Display", serif;
    font-size: 22px;
    letter-spacing: 2px;
    fill: var(--ink);
    text-anchor: middle;
  }
  .arc-claim {
    font-family: "Dancing Script", cursive;
    font-size: 42px;
    fill: var(--ink);
  }
  .product-type {
    font-family: "Dancing Script", cursive;
    font-weight: 700;
    font-size: 84px;
    fill: var(--ink);
    text-anchor: middle;
  }
  .tagline {
    font-family: "Dancing Script", cursive;
    font-weight: 700;
    font-size: 50px;
    fill: var(--olive-light);
    text-anchor: middle;
  }
</style>
</head>
<body>
<main class="canvas">
  <svg class="label-art" width="1085" height="1200" viewBox="0 0 1085 1200">
    <defs>
      <path id="arc-left" d="M150,450 A420 420 0 0 1 415,215"/>
      <path id="arc-right" d="M670,215 A420 420 0 0 1 935,450"/>
      <linearGradient id="frond-tone" x1="0" y1="0" x2="0" y2="1">
        <stop offset="0" stop-color="var(--leaf-light)"/>
        <stop offset="1" stop-color="var(--leaf)"/>
      </linearGradient>
    </defs>

    <ellipse class="label-disc" cx="542" cy="600" rx="470" ry="480" fill="var(--label)"/>

    <g class="brand-mark">
      <circle cx="542" cy="195" r="46" fill="var(--ink)"/>
      <text class="brand-name" x="542" y="278">TIDEWELL GOODS</text>
    </g>

    <text class="arc-claim"><textPath href="#arc-left" startOffset="50%" text-anchor="middle">Hand harvested</textPath></text>
    <text class="arc-claim"><textPath href="#arc-right" startOffset="50%" text-anchor="middle">Naturally processed</textPath></text>

    <text class="title title-amber" x="542" y="455" font-size="128">AMBER</text>
    <text class="title title-frond" x="542" y="655" font-size="210" font-weight="500">FROND</text>

    <text class="product-type" x="542" y="760">Meal</text>

    <text class="tagline" x="542" y="840">The Food Tonic</text>
    <text class="tagline" x="542" y="895">of the Sea</text>

    <g class="frond-illustration" role="img" aria-label="Green seaweed fronds illustration, left">
      <ellipse cx="255" cy="780" rx="55" ry="110" transform="rotate(-40 255 780)" fill="url(#frond-tone)"/>
    </g>
    <g class="frond-illustration" role="img" aria-label="Green seaweed fronds illustration, right">
      <ellipse cx="830" cy="820" rx="55" ry="110" transform="rotate(35 830 820)" fill="url(#frond-tone)"/>
    </g>
  </svg>
</main>
</body>
</html>
```